Business card design for a Cloud Service Provider Company

We already have business card and would like to update and get a different design. Our company is Managed IT services and Cloud Solutions Company, Dorlen Systems. Attached is our current logo, current business card and sample design. I am not sure if we still need to keep our partners details on the back of the card as it does not look good to me... Please let me know if you need any additional information...

Target Market(s)

Any verticals with IT infrastructure - CEOs, CFOs and CIOs

Industry/Entity Type

Information Technology

Requirements
Must have
• First Name Last Name
• Phone
• Email address
• Company Logo

```html
<!DOCTYPE html>
<html lang="en">
<head>
<meta charset="utf-8">
<title>Dorlen Systems — Business Card</title>
<link href="https://fonts.googleapis.com/css2?family=Lato:wght@400;700;900&display=swap" rel="stylesheet">
<style>
  :root {
    --backdrop: #2b2b2b;
    --card: #f4f4f4;
    --ink: #2a2a2a;
    --ink-soft: #3a3a3a;
    --brand-blue: #1d8fc0;
    --brand-green: #8cc21f;
    --accent-dot: #2aa6d8;
  }
  * { margin: 0; padding: 0; box-sizing: border-box; }
  html, body {
    width: 1200px; height: 997px; overflow: hidden;
    background: var(--backdrop);
    font-family: "Lato", Arial, sans-serif;
  }
  .stage { position: relative; width: 1200px; height: 997px; }

  .card {
    position: absolute;
    width: 580px; height: 330px;
    background: var(--card);
    border-radius: 18px;
    box-shadow: 0 20px 40px rgba(0,0,0,0.45);
  }
  .card--front { left: 90px; top: 110px; display: flex; align-items: center; justify-content: center; }
  .card--back { left: 530px; top: 530px; }

  .wordmark {
    display: flex; align-items: center; gap: 14px;
    color: var(--ink); font-weight: 700; letter-spacing: -0.5px;
  }
  .wordmark__dot { border-radius: 50%; background: var(--brand-blue); }
  .card--front .wordmark { font-size: 54px; }
  .card--front .wordmark__dot { width: 26px; height: 26px; }

  .card--back .wordmark { position: absolute; top: 34px; right: 38px; font-size: 28px; gap: 8px; }
  .card--back .wordmark__dot { width: 14px; height: 14px; }

  .rule {
    position: absolute; left: 200px; right: 38px; top: 150px;
    height: 2px; background: var(--brand-green);
  }
  .holder { position: absolute; left: 40px; top: 130px; }
  .holder__name { color: var(--brand-blue); font-weight: 900; font-size: 21px; line-height: 1.1; }
  .holder__role { color: var(--brand-green); font-weight: 700; font-size: 13px; letter-spacing: 0.5px; margin-top: 2px; }

  .contacts { position: absolute; left: 40px; top: 202px; list-style: none; }
  .contacts li {
    display: flex; align-items: flex-start; gap: 12px;
    color: var(--ink-soft); font-size: 14px; line-height: 1.3; margin-bottom: 9px;
  }
  .contacts svg { flex: 0 0 18px; width: 18px; height: 18px; margin-top: 1px; }

  .site { position: absolute; right: 38px; top: 172px; color: var(--brand-blue); font-weight: 700; font-size: 14px; }
</style>
</head>
<body>
<main class="stage">
  <section class="card card--front" aria-label="Card front">
    <div class="wordmark"><span class="wordmark__dot"></span><span>Dorlen Systems</span></div>
  </section>

  <section class="card card--back" aria-label="Card back">
    <div class="wordmark"><span class="wordmark__dot"></span><span>Dorlen Systems</span></div>
    <div class="rule"></div>
    <div class="holder">
      <div class="holder__name">Maren Kolbeck</div>
      <div class="holder__role">FOUNDER &amp; CEO</div>
    </div>
    <div class="site">www.dorlensystems.com</div>
    <ul class="contacts">
      <li>
        <svg viewBox="0 0 18 18" aria-hidden="true"><circle cx="9" cy="9" r="9" fill="var(--accent-dot)"/><path d="M6 5.5c.5-.5 1.2-.3 1.5.3l.6 1.1c.2.4 0 .8-.3 1l-.4.3c.4 1 1.2 1.8 2.2 2.2l.3-.4c.2-.3.7-.5 1-.3l1.1.6c.6.3.8 1 .3 1.5-.8.9-2 1-3 .4-1.6-.8-2.9-2.1-3.7-3.7-.6-1-.5-2.2.4-3z" fill="#fff"/></svg>
        <span>+1 (555) 014-2268</span>
      </li>
      <li>
        <svg viewBox="0 0 18 18" aria-hidden="true"><circle cx="9" cy="9" r="9" fill="var(--accent-dot)"/><rect x="4.5" y="5.8" width="9" height="6.4" rx="0.8" fill="#fff"/><path d="M4.9 6.3 9 9.4l4.1-3.1" fill="none" stroke="var(--accent-dot)" stroke-width="1"/></svg>
        <span>maren@dorlensystems.com</span>
      </li>
      <li>
        <svg viewBox="0 0 18 18" aria-hidden="true"><circle cx="9" cy="9" r="9" fill="var(--accent-dot)"/><path d="M9 4a3 3 0 0 0-3 3c0 2.3 3 6.5 3 6.5s3-4.2 3-6.5a3 3 0 0 0-3-3zm0 4.2a1.2 1.2 0 1 1 0-2.4 1.2 1.2 0 0 1 0 2.4z" fill="#fff"/></svg>
        <span>18 Alder Court, 1st Floor,<br>Westbrook, CT 06498</span>
      </li>
    </ul>
  </section>
</main>
</body>
</html>
```